Small consulting business needs logo and business card design

I need a logo, business card and letterhead design for a small consulting firm called Veltramo Consulting. My customers are generally small to medium sized businesses but I have done work for major corporates and government departments. The field of consulting is strategic/business planning and program management. I have blue as the predominate colour in my current business card but I am happy to change this for the right design
Industry/Entity Type
Business

```html
<!DOCTYPE html>
<html lang="en">
<head>
<meta charset="utf-8">
<title>Veltramo Consulting — Letterhead</title>
<link rel="stylesheet" href="https://fonts.googleapis.com/css2?family=Tinos:wght@400;700&display=swap">
<style>
  :root {
    --backdrop: #e8e8e8;
    --paper: #ffffff;
    --orange: #f0981f;
    --navy: #33326d;
    --arrow-red: #e0462c;
    --arrow-sky: #3fa9e0;
    --text-light: #ffffff;
  }
  html, body {
    margin: 0;
    width: 1200px;
    height: 795px;
    overflow: hidden;
    background: var(--backdrop);
  }
  .canvas {
    position: relative;
    width: 1200px;
    height: 795px;
  }
  .letterhead {
    position: absolute;
    left: 338px;
    top: 27px;
    width: 523px;
    height: 740px;
    background: var(--paper);
    box-shadow: 0 2px 10px rgba(0,0,0,0.12);
    overflow: hidden;
    font-family: "Tinos", "Times New Roman", serif;
  }
  .letterhead__bands {
    position: absolute;
    inset: 0;
  }
  .band--top { fill: var(--orange); }
  .band--bottom { fill: var(--navy); }
  .arrow--top { stroke: var(--arrow-red); }
  .arrow--bottom { stroke: var(--arrow-sky); }
  .arrow { fill: none; stroke-width: 1.4; }

  .brand {
    position: absolute;
    top: 28px;
    right: 16px;
    display: flex;
    align-items: center;
    gap: 7px;
  }
  .brand__square {
    width: 14px;
    height: 14px;
    background: var(--orange);
  }
  .brand__name {
    font-size: 21px;
    font-weight: 400;
    color: var(--navy);
    line-height: 1;
    white-space: nowrap;
  }

  .website {
    position: absolute;
    left: 52px;
    top: 62px;
    font-size: 11px;
    font-weight: 700;
    color: var(--text-light);
    letter-spacing: 0.2px;
  }

  .contact {
    position: absolute;
    right: 24px;
    top: 648px;
    margin: 0;
    font-style: normal;
    font-size: 11px;
    font-weight: 700;
    line-height: 1.35;
    color: var(--text-light);
    text-align: left;
  }
</style>
</head>
<body>
<main class="canvas">
  <article class="letterhead">
    <svg class="letterhead__bands" width="523" height="740" viewBox="0 0 523 740" aria-hidden="true">
      <polygon class="band band--top" points="0,0 423,0 296,88 0,88"/>
      <polygon class="band band--bottom" points="523,740 209,740 377,612 523,612"/>
      <path class="arrow arrow--top" d="M2,58 L24,70 L2,82 M2,70 L24,70"/>
      <path class="arrow arrow--bottom" d="M510,620 L490,634 L505,642 M490,634 L512,634"/>
    </svg>

    <header class="brand">
      <span class="brand__square"></span>
      <span class="brand__name">Veltramo Consulting</span>
    </header>

    <p class="website">www.veltramoconsulting.com</p>

    <address class="contact">
      Street Address<br>
      1234 567 890<br>
      hello@veltramo.com
    </address>
  </article>
</main>
</body>
</html>
```